Introduction of new dentist and new treatments

We want inform our Patients of our new dentist and new treatment methods. It is dealing about biologic dentistry and holistic dentistry. we are in switzerland and speak german

Font styles to use
Sans Serif

Colors
00a990
33b8a4
9bcb3c
acd036
cadf82
0292cd
3176b5
e34297
e667a6

Requirements
Must have
• Text, which can be edited. It will be in german
• Name of the dental clinic is
• "Velmora - Ihr Zahnarzt in Zug"
Nice to have
• A4 Layout

```html
<!DOCTYPE html>
<html lang="de">
<head>
<meta charset="utf-8">
<title>Velmora – Interdisziplinäre Zahnmedizin</title>
<link href="https://fonts.googleapis.com/css2?family=Open+Sans:wght@400;600;700;800&display=swap" rel="stylesheet">
<style>
  :root {
    --blue-deep: #3176b5;
    --blue-bright: #0292cd;
    --green: #00a990;
    --lime: #9bcb3c;
    --lime-strong: #4fb847;
    --pink: #e34297;
    --ink: #2b2f36;
    --text: #4a4f57;
    --page-bg: #eef0f3;
    --paper: #ffffff;
  }
  * { box-sizing: border-box; margin: 0; padding: 0; }
  html, body { width: 1200px; height: 800px; overflow: hidden; }
  body {
    background: var(--page-bg);
    font-family: "Open Sans", Arial, sans-serif;
    color: var(--text);
    position: relative;
  }
  .flyer {
    position: absolute;
    left: 330px; top: 18px;
    width: 540px; height: 764px;
    background: var(--paper);
    overflow: hidden;
    box-shadow: 0 4px 18px rgba(0,0,0,.12);
  }
  .header-bg { position: absolute; left: 0; top: 0; width: 540px; height: 260px; }
  .portrait {
    position: absolute;
    left: 290px; top: 22px; width: 250px; height: 200px;
    background: linear-gradient(180deg, #dfe6ef 0%, #d6c3b4 38%, #c9b0a0 56%, #1f66c0 76%, #1a5bb0 100%);
  }
  .header-swoosh { position: absolute; left: 0; top: 0; width: 540px; height: 260px; }
  .brand { position: absolute; left: 36px; top: 128px; }
  .brand-name {
    font-size: 28px; font-weight: 600; letter-spacing: 6px;
    color: var(--blue-deep); line-height: 1;
  }
  .brand-tagline {
    margin-top: 6px; padding-left: 66px;
    font-size: 10.5px; color: var(--ink);
  }
  .headline {
    position: absolute; left: 36px; top: 262px; width: 450px;
    font-size: 17px; line-height: 1.22; font-weight: 800;
    color: var(--blue-deep);
  }
  .intro {
    position: absolute; left: 36px; top: 332px; width: 470px;
    font-size: 10.5px; line-height: 1.38; font-weight: 700; color: var(--ink);
  }
  .columns {
    position: absolute; left: 36px; top: 388px; width: 470px;
    display: grid; grid-template-columns: 1fr 1fr; column-gap: 22px;
  }
  .section { margin-bottom: 11px; }
  .section-title {
    font-size: 11.5px; line-height: 1.2; font-weight: 800;
    color: var(--blue-bright); margin-bottom: 4px;
  }
  .section-text { font-size: 8px; line-height: 1.4; text-align: justify; hyphens: auto; }
  .footer-wave { position: absolute; left: 0; bottom: 0; width: 540px; height: 130px; }
  .contact { position: absolute; right: 30px; top: 664px; }
  .contact-phone {
    display: flex; align-items: center; gap: 6px;
    font-size: 14px; font-weight: 800; color: var(--blue-deep);
  }
  .contact-web { font-size: 10.5px; color: var(--ink); margin-top: 2px; padding-left: 20px; }
  .address-pill {
    position: absolute; left: 28px; top: 716px;
    height: 30px; width: 290px; border-radius: 15px;
    background: var(--lime-strong);
    display: flex; align-items: center; gap: 8px; padding-left: 14px;
    font-size: 11px; font-weight: 600; color: #fff;
  }
</style>
</head>
<body>
  <article class="flyer">
    <svg class="header-bg" viewBox="0 0 540 260" aria-hidden="true">
      <defs>
        <linearGradient id="headerTint" x1="0" y1="0" x2="1" y2="1">
          <stop offset="0" stop-color="#eef2f8"/>
          <stop offset="1" stop-color="#d9e1ec"/>
        </linearGradient>
      </defs>
      <rect width="540" height="260" fill="url(#headerTint)"/>
    </svg>

    <div class="portrait" role="img" aria-label="Porträtfoto des neuen Zahnarztes im blauen Polohemd"></div>

    <svg class="header-swoosh" viewBox="0 0 540 260" aria-hidden="true">
      <path d="M0 260 L0 248 C180 232 360 200 540 160 L540 260 Z" fill="#ffffff"/>
      <path d="M0 244 C180 226 360 192 540 146" fill="none" stroke="var(--blue-deep)" stroke-width="8"/>
      <path d="M230 234 C340 218 440 194 540 164" fill="none" stroke="var(--lime-strong)" stroke-width="4"/>
    </svg>

    <div class="brand">
      <div class="brand-name">VELMORA</div>
      <div class="brand-tagline">Ihr Zahnarzt in Zug</div>
    </div>

    <h1 class="headline">Interdisziplinäre Zahnmedizin:<br>Zusammenhang zwischen Zahnproblemen und der Gesundheit von Körper und Geist</h1>

    <p class="intro">Zahn und Gesundheit haben eins gemeinsam: Man vermisst sie, wenn sie fehlt. Zähne haben einen engen Zusammenhang zur Gesundheit und können diese beeinflussen. Sowohl negativ als auch positiv.</p>

    <div class="columns">
      <div class="column">
        <section class="section">
          <h2 class="section-title">Funktion des Kauorgans und interdisziplinäre Zahnmedizin</h2>
          <p class="section-text">Funktion ist nicht alles. Aber ohne Funktion ist alles nichts. Das Kauorgan steht in enger Verbindung mit Kopf, Nacken und Haltung. Eine gut abgestimmte Zusammenarbeit von Zahnmedizin, Physiotherapie und Osteopathie bringt Kiefer und Körper wieder ins Gleichgewicht. So lassen sich Verspannungen, Kopfschmerzen und Beschwerden im Kiefergelenk gezielt lindern.</p>
        </section>
        <section class="section">
          <h2 class="section-title">Parodontitis und systemische Erkrankungen</h2>
          <p class="section-text">Parodontitis, die Entzündung des Zahnhalteapparats, zählt zu den häufigsten chronischen Krankheiten weltweit. Sie steht im Zusammenhang mit Diabetes, Herz-Kreislauf-Erkrankungen und Frühgeburten. Zahnfleischbluten und Zahnlockerung sind typische Warnzeichen. Eine frühe, systematische Behandlung schützt nicht nur die Zähne, sondern wirkt sich positiv auf die gesamte Gesundheit aus.</p>
        </section>
      </div>
      <div class="column">
        <section class="section">
          <h2 class="section-title">Zahnverlust und neurologische Auswirkungen</h2>
          <p class="section-text">Ein gesundes Kausystem hat viele Aufgaben. Beim Kauen werden Nerven und Gehirn angeregt, die Durchblutung steigt. Fehlen Zähne, nimmt diese Anregung ab. Studien zeigen, dass Menschen mit wenigen eigenen Zähnen ein höheres Risiko für Demenz tragen.</p>
        </section>
        <section class="section">
          <h2 class="section-title">Ganzheitliche Erkenntnisse</h2>
          <p class="section-text">Die biologische Zahnmedizin betrachtet den Menschen als Ganzes. Zähne und Organe sind über Meridiane verbunden. Wir setzen auf verträgliche Materialien und schonende Methoden. Gemeinsam mit Ihnen finden wir die Behandlung, die zu Ihrer Gesundheit und Lebenssituation passt.</p>
        </section>
      </div>
    </div>

    <svg class="footer-wave" viewBox="0 0 540 130" aria-hidden="true">
      <path d="M380 130 C440 104 480 52 540 16 L540 130 Z" fill="#cfe3f3"/>
      <path d="M440 130 C480 104 505 72 540 56 L540 130 Z" fill="var(--blue-bright)"/>
    </svg>

    <div class="contact">
      <div class="contact-phone">
        <svg width="14" height="14" viewBox="0 0 24 24" aria-hidden="true"><path fill="var(--blue-deep)" d="M6.6 10.8a15.1 15.1 0 0 0 6.6 6.6l2.2-2.2a1 1 0 0 1 1-.25 11.4 11.4 0 0 0 3.6.57 1 1 0 0 1 1 1V20a1 1 0 0 1-1 1A17 17 0 0 1 3 4a1 1 0 0 1 1-1h3.5a1 1 0 0 1 1 1c0 1.25.2 2.45.57 3.6a1 1 0 0 1-.25 1z"/></svg>
        +41 41 555 20 48
      </div>
      <div class="contact-web">www.velmora-zug.ch</div>
    </div>

    <div class="address-pill">
      <svg width="12" height="16" viewBox="0 0 12 16" aria-hidden="true"><path fill="#fff" d="M6 0a6 6 0 0 0-6 6c0 4.5 6 10 6 10s6-5.5 6-10a6 6 0 0 0-6-6zm0 8.2A2.2 2.2 0 1 1 6 3.8a2.2 2.2 0 0 1 0 4.4z"/></svg>
      Zahnarztpraxis Seestrasse 18, 6300 Zug
    </div>
  </article>
</body>
</html>
```